Walk Through Fire Step out, step up and into your best performance

BRIEF FOR BOOK FRONT COVER

• It needs to be iconic
• It needs to be a ‘clean’ design
• Needs to be seen on a bookshelf in an airport from 50 feet away
• No stick like figures/cartoon style or cutesy design
• The book appeals to both male and female readers
• This is a cross over book and covers a couple of genres like Martin Kessler’s book Small Steady Gains or Tessa Holm’s Quiet Mastery. So it is primarily about taking better care of yourself personally, professionally and will appeal to those in business.
• The idea that a personal enriching life feeds into an engaged performer on the job – they feed off each other leading to increased engagement, productivity and fulfillment
• The dance analogy means that you are not sitting on the sidelines of your life or business
• It is laced with inspiring real life case studies
• Positioning of the book: People facing adversity and still come through better than ever and better equipped to what comes next.
• Want a cover that would attract a Pinnacle 40 CEO to buy the book for his staff
• My name as the author should be across the bottom MIRIAM FOSTER MBA MCC
Updates

Project Deadline Extended Reason: A big thank you for all the designers who submitted a cover design and I have been spoilt for choiceI need to finalize the copy on the book cover and hence the need for an extension of time.Thanks for your understanding.Miriam Added Sunday, September 18, 2016

Target Market(s)

Professionals in the age group 25 - 55

Industry/Entity Type

Airport

Contact Information for Business Card

basic information and a very clean look

Logo Text

probably book title more important that it can be seen clearly when the size is reduced to a small size e.g. if sponsoring an event

Number of Pages Required

5+ page

Font styles to use
Sans Serif

Colors
ec1f27
f37122
abd037

Requirements
Must have
• info already provided

```html
<!DOCTYPE html>
<html lang="en">
<head>
<meta charset="utf-8">
<title>Walk Through Fire – Miriam Foster</title>
<link rel="stylesheet" href="https://fonts.googleapis.com/css2?family=Archivo+Black&family=Cinzel:wght@700&display=swap">
<style>
  :root {
    --paper: #ffffff;
    --rain-deep: #2c5558;
    --rain-mid: #5f8a7c;
    --rain-light: #b9d08f;
    --grass: #4f8a3a;
    --grass-dark: #2f6a2c;
    --ink: #1a1a1a;
    --rule: #c9c9c9;
    --figure: #151515;
  }
  html, body {
    margin: 0;
    padding: 0;
    width: 848px;
    height: 1200px;
    overflow: hidden;
    background: var(--paper);
  }
  .cover {
    position: relative;
    width: 848px;
    height: 1200px;
    background: var(--paper);
  }
  .cover-art {
    position: absolute;
    inset: 0;
    width: 848px;
    height: 1200px;
  }
  .title-text {
    font-family: "Archivo Black", "Arial Black", sans-serif;
  }
  .dancer {
    fill: var(--figure);
  }
  .subtitle {
    position: absolute;
    left: 24px;
    top: 878px;
    width: 800px;
    margin: 0;
    text-align: center;
    text-transform: uppercase;
    font-family: "Cinzel", Georgia, serif;
    font-weight: 700;
    font-size: 26px;
    line-height: 36px;
    letter-spacing: 3px;
    color: var(--grass);
    background: linear-gradient(180deg, var(--grass-dark), var(--rain-light) 55%, var(--grass));
    -webkit-background-clip: text;
    background-clip: text;
    -webkit-text-fill-color: transparent;
  }
  .author {
    position: absolute;
    left: 0;
    top: 1036px;
    width: 848px;
    margin: 0;
    text-align: center;
    font-family: "Archivo Black", "Arial Black", sans-serif;
    font-size: 62px;
    line-height: 66px;
    letter-spacing: 2px;
    color: var(--grass);
  }
  .credentials {
    position: absolute;
    left: 0;
    top: 1104px;
    width: 848px;
    margin: 0;
    text-align: center;
    font-family: "Cinzel", Georgia, serif;
    font-weight: 700;
    font-size: 32px;
    line-height: 40px;
    letter-spacing: 2px;
    color: var(--ink);
  }
</style>
</head>
<body>
<main class="cover">
  <svg class="cover-art" viewBox="0 0 848 1200" xmlns="http://www.w3.org/2000/svg" aria-labelledby="book-title">
    <title id="book-title">Walk Through Fire</title>
    <defs>
      <linearGradient id="title-fill" gradientUnits="userSpaceOnUse" x1="0" y1="30" x2="0" y2="745">
        <stop offset="0" stop-color="#2c5558"/>
        <stop offset="0.3" stop-color="#4c7670"/>
        <stop offset="0.55" stop-color="#8aab7e"/>
        <stop offset="0.8" stop-color="#b9d08f"/>
        <stop offset="1" stop-color="#9fc27a"/>
      </linearGradient>
      <linearGradient id="rule-fade" x1="0" x2="1" y1="0" y2="0">
        <stop offset="0" stop-color="#c9c9c9" stop-opacity="0"/>
        <stop offset="0.5" stop-color="#8a8a8a"/>
        <stop offset="1" stop-color="#c9c9c9" stop-opacity="0"/>
      </linearGradient>
    </defs>

    <g class="title-text" fill="url(#title-fill)">
      <text x="24" y="230" font-size="250" textLength="800" lengthAdjust="spacingAndGlyphs">WALK</text>
      <text x="62" y="510" font-size="250" textLength="728" lengthAdjust="spacingAndGlyphs">THROUGH</text>
      <text x="152" y="742" font-size="210" textLength="540" lengthAdjust="spacingAndGlyphs">FIRE</text>
    </g>

    <rect x="0" y="853" width="848" height="3" fill="url(#rule-fade)"/>
    <rect x="0" y="984" width="848" height="3" fill="url(#rule-fade)"/>

    <g role="img" aria-label="Silhouette of a man dancing, arm raised, pushing up the title">
      <rect class="dancer" x="100" y="612" width="44" height="244" rx="14"/>
    </g>
    <g role="img" aria-label="Silhouette of a woman dancing with both arms raised">
      <rect class="dancer" x="694" y="604" width="44" height="252" rx="14"/>
    </g>
  </svg>

  <p class="subtitle">Step out, step up and step into<br>your best performance</p>
  <h2 class="author">MIRIAM FOSTER</h2>
  <p class="credentials">MBA MCC</p>
</main>
</body>
</html>
```